DENTIST OFFICE POST CARD DESIGN

COMPANY NAME: BEARABLE DENTISTRYCome and see if Quillmoor Dentistry is for you.... ALWAYSWELCOMINGNEW PATIENTS!Call today for your appointment!607 555 0183 We are located on 7 Penwick Street , Harrowby Vale----(map scketch)All in one stop for all your dental care needsCOSMETIC DENTISTRYDENTAL IMPLANTSROOT CANALSVENEERSWHITENINGSFILLINGSCROWNSBRIDGESDENTURESEXTRACTIONSGUM TREATMENTSSNAP ON SMILECOLOR------ANYPOSTCARD INDICIA;PRSRT STDECRWSSU.S. POSTAGEPAIDEDDM RETAILLocalPostal Customer

```html
<!DOCTYPE html>
<html lang="en">
<head>
<meta charset="utf-8">
<title>Quillmoor Dentistry Postcard</title>
<link href="https://fonts.googleapis.com/css2?family=Fugaz+One&family=Ubuntu:wght@400;500;700&display=swap" rel="stylesheet">
<style>
  :root {
    --blue: #0b73c4;
    --blue-deep: #0a5ea8;
    --blue-light: #2a8fd8;
    --pale: #dfe9f7;
    --yellow: #f5e90f;
    --white: #ffffff;
    --stage: #e8ebef;
    --map-base: #1a7fcc;
  }
  * { margin: 0; padding: 0; box-sizing: border-box; }
  html, body { width: 886px; height: 1200px; overflow: hidden; background: var(--stage); }
  .canvas { position: relative; width: 886px; height: 1200px; }

  .spread { position: absolute; top: 0; left: 0; width: 886px; height: 608px; display: flex; }
  .panel { position: relative; width: 443px; height: 608px; overflow: hidden; }
  .panel-inside-left { background: linear-gradient(180deg, var(--blue-light), var(--blue) 45%, var(--blue-deep)); }
  .panel-inside-right { background: radial-gradient(ellipse at 50% 40%, var(--blue-light), var(--blue) 60%, var(--blue-deep)); }
  .panel-art { position: absolute; inset: 0; width: 100%; height: 100%; }

  .tilted { position: absolute; left: 0; width: 443px; transform: rotate(-5deg); transform-origin: center; text-align: center; }
  .headline { top: 46px; left: 10px; text-align: left; font-family: "Fugaz One", sans-serif; font-size: 19px; color: var(--blue-deep); letter-spacing: 0.5px; }
  .call { top: 140px; left: 145px; width: 260px; text-align: left; border-left: 2px solid var(--yellow); padding-left: 8px; }
  .call-lead { font-family: "Ubuntu", sans-serif; font-size: 14px; color: var(--white); }
  .call-number { font-family: "Ubuntu", sans-serif; font-weight: 700; font-size: 33px; color: var(--yellow); line-height: 1.05; }
  .tagline { top: 285px; font-family: "Ubuntu", sans-serif; font-size: 15px; color: var(--white); }
  .services { top: 382px; font-family: "Fugaz One", sans-serif; font-size: 18px; line-height: 1.3; color: var(--yellow); }

  .location { position: absolute; top: 112px; width: 100%; text-align: center; }
  .location-lead { font-family: "Ubuntu", sans-serif; font-size: 19px; color: var(--white); }
  .location-address { font-family: "Fugaz One", sans-serif; font-size: 19px; color: var(--yellow); }
  .map-area { position: absolute; left: 30px; top: 270px; width: 390px; height: 300px;
    background: radial-gradient(ellipse at 40% 50%, rgba(185,211,154,0.85) 0 12%, rgba(26,127,204,0.6) 40%, rgba(11,115,196,0) 72%); }

  .cover { position: absolute; left: 223px; top: 650px; width: 440px; height: 520px; overflow: hidden;
    background: radial-gradient(ellipse at 40% 35%, var(--blue-light), var(--blue) 55%, var(--blue-deep));
    box-shadow: 0 6px 18px rgba(0,0,0,0.25); }
  .cover-name { position: absolute; top: 220px; width: 100%; text-align: center; font-family: "Fugaz One", sans-serif; font-size: 30px; color: var(--white); letter-spacing: 1px; }
  .cover-name::before { content: ""; display: block; width: 14px; height: 14px; margin: 0 auto 14px; border-radius: 50%; background: var(--yellow); }
  .cover-invite { position: absolute; bottom: 40px; width: 100%; text-align: center; font-family: "Ubuntu", sans-serif; font-size: 14px; color: var(--yellow); }
</style>
</head>
<body>
<div class="canvas">
  <section class="spread">
    <div class="panel panel-inside-left">
      <svg class="panel-art" viewBox="0 0 443 608" aria-hidden="true">
        <defs>
          <linearGradient id="topBand" x1="0" y1="0" x2="1" y2="0">
            <stop offset="0" stop-color="#ffffff"/><stop offset="1" stop-color="#9fc0ea"/>
          </linearGradient>
          <linearGradient id="bottomBand" x1="0" y1="1" x2="1" y2="0">
            <stop offset="0" stop-color="#3f8fe0"/><stop offset="1" stop-color="#e6eefa"/>
          </linearGradient>
          <linearGradient id="streak" x1="0" y1="0" x2="1" y2="0">
            <stop offset="0" stop-color="#fff" stop-opacity="0"/><stop offset="0.5" stop-color="#fff" stop-opacity="0.55"/><stop offset="1" stop-color="#fff" stop-opacity="0"/>
          </linearGradient>
        </defs>
        <polygon points="0,0 443,0 443,46 0,102" fill="url(#topBand)"/>
        <line x1="0" y1="130" x2="443" y2="86" stroke="url(#streak)" stroke-width="2"/>
        <polygon points="80,110 360,84 360,90 80,116" fill="url(#streak)" opacity="0.5"/>
        <line x1="0" y1="290" x2="443" y2="212" stroke="url(#streak)" stroke-width="2"/>
        <polygon points="90,255 380,225 380,232 90,262" fill="url(#streak)" opacity="0.5"/>
        <line x1="0" y1="378" x2="443" y2="302" stroke="url(#streak)" stroke-width="2"/>
        <polygon points="60,350 330,320 330,327 60,357" fill="url(#streak)" opacity="0.5"/>
        <polygon points="0,560 443,537 443,608 0,608" fill="url(#bottomBand)"/>
        <g class="phone-icon" fill="none" stroke="#f5e90f" stroke-width="4">
          <circle cx="93" cy="192" r="33"/>
          <path d="M80 175 q-4 8 6 24 q10 14 20 16 l6 -7 l-9 -7 l-5 4 q-8 -4 -12 -14 l5 -4 l-4 -10 z" fill="#f5e90f" stroke-width="1.5"/>
        </g>
      </svg>
      <p class="tilted headline">ALWAYS WELCOMING NEW PATIENTS!</p>
      <div class="tilted call">
        <p class="call-lead">Call today for your appointment!</p>
        <p class="call-number">607 555 0183</p>
      </div>
      <p class="tilted tagline">All in one stop for all your dental care needs</p>
      <p class="tilted services">Cosmetic Dentistry Dental<br>Implantsroot | Canals<br>Veneers | Whitenings<br>Fillings | Crowns | Bridges<br>Denture Sextractions | Gum Treatments<br>Glide In Grincolor</p>
    </div>
    <div class="panel panel-inside-right">
      <div class="location">
        <p class="location-lead">We are located on:</p>
        <p class="location-address">7 Penwick Street , Harrowby Vale</p>
      </div>
      <div class="map-area" role="img" aria-label="Street map sketch showing the route to the office near the park"></div>
    </div>
  </section>

  <section class="cover">
    <p class="cover-name">Quillmoor Dentistry</p>
    <p class="cover-invite">Come and see if Quillmoor Dentistry is for you....</p>
  </section>
</div>
</body>
</html>
```